BENEATH THE [HARBOR] OF A DAWN, Mend your road

We are looking for a cover refresh of an existing bestselling book that is going into 3rd edition print this year.
The book is an inspirational as well as educational book that has become recognized as one of the most comprehensive, actionable, personal and financial planning resources available today for families, individuals and business owners alike.
Comprised of three true stories of loss, learning to live and love again and a 30 page checklist at the back of the book it contains tips and strategies for everyone to help them to get their personal and financial lives in order while they can.
The cover must have the following:
1. Appeal to a broad audience/both personal and corporate
2. Include Mara Quellton Bestselling Author
3. Include introduction of a new Afterword
4. 3rd Edition
5. Colors to remain the same – red, black and white
6. The title must remain in caps and the word [HARBOR] must have the brackets around it
We have also added a current copy of the second edition to help you. For your information our website is www.thequelltonhouse.example
Reason: We have narrowed it down to our top 3 designs. We are submitting the covers to our community for them to pick the top cover. Good luck to everyone

```html
<!DOCTYPE html>
<html lang="en">
<head>
<meta charset="utf-8">
<title>Beneath the [Harbor] of a Dawn — Mara Quellton</title>
<link rel="stylesheet" href="https://fonts.googleapis.com/css2?family=Noto+Serif:wght@400;700&family=Dancing+Script:wght@600;700&display=swap">
<style>
  :root {
    --ink: #111111;
    --paper: #ffffff;
    --accent: #c8070c;
    --shade: #e6e6e6;
  }
  html, body {
    margin: 0;
    padding: 0;
    width: 800px;
    height: 1200px;
    overflow: hidden;
    background: var(--paper);
  }
  .cover {
    display: block;
    width: 800px;
    height: 1200px;
  }
  .cover__frame { fill: none; stroke: var(--ink); stroke-width: 3; }
  .cover__title { font-family: "Noto Serif", Georgia, serif; font-weight: 400; fill: var(--ink); }
  .cover__title--accent { fill: var(--accent); }
  .cover__title--ink { fill: var(--ink); }
  .badge__disc { fill: var(--accent); }
  .badge__number { font-family: "Noto Serif", Georgia, serif; font-style: italic; fill: var(--paper); }
  .badge__script { font-family: "Dancing Script", cursive; font-weight: 700; fill: var(--paper); }
  .badge__ring { font-family: "Noto Serif", Georgia, serif; font-size: 17px; fill: var(--ink); }
  .badge__ring--accent { fill: var(--accent); }
  .author__label { font-family: "Noto Serif", Georgia, serif; font-size: 17px; letter-spacing: 6px; fill: var(--ink); }
  .author__band { fill: var(--accent); }
  .author__name { font-family: "Noto Serif", Georgia, serif; font-size: 54px; fill: var(--paper); }
</style>
</head>
<body>
<svg class="cover" viewBox="0 0 800 1200" xmlns="http://www.w3.org/2000/svg">
  <defs>
    <radialGradient id="quillShade" cx="0.45" cy="0.5" r="0.6">
      <stop offset="0" stop-color="#cfcfcf"/>
      <stop offset="1" stop-color="#ffffff"/>
    </radialGradient>
    <path id="badgeArc" d="M562 998.6 A100 100 0 1 1 662 998.6"/>
  </defs>

  <rect class="cover__frame" x="24" y="24" width="752" height="1152"/>

  <g class="cover__title">
    <text x="408" y="142" font-size="104" text-anchor="middle" textLength="640" lengthAdjust="spacingAndGlyphs">BENEATH THE</text>
    <text x="408" y="300" font-size="136" text-anchor="middle" textLength="632" lengthAdjust="spacingAndGlyphs"><tspan class="cover__title--accent">[HARB</tspan><tspan class="cover__title--ink">O</tspan><tspan class="cover__title--accent">R]</tspan></text>
    <text x="400" y="452" font-size="128" text-anchor="middle" textLength="624" lengthAdjust="spacingAndGlyphs">OF A DAWN</text>
  </g>

  <rect class="cover__illustration" x="112" y="505" width="460" height="480" fill="url(#quillShade)" role="img" aria-label="Black quill feather writing a looping ink line"/>

  <g class="badge">
    <circle class="badge__disc" cx="612" cy="912" r="84"/>
    <text class="badge__number" x="600" y="922" font-size="68" text-anchor="middle">3</text>
    <text class="badge__script" x="648" y="890" font-size="26" text-anchor="middle">rd</text>
    <text class="badge__script" x="614" y="968" font-size="30" text-anchor="middle">edition</text>
    <text class="badge__ring">
      <textPath href="#badgeArc" textLength="505" lengthAdjust="spacing">Introduction of a new <tspan class="badge__ring--accent">Afterword</tspan></textPath>
    </text>
  </g>

  <g class="author">
    <text class="author__label" x="400" y="1077" text-anchor="middle">BESTSELLING AUTHOR</text>
    <rect class="author__band" x="0" y="1086" width="800" height="66"/>
    <text class="author__name" x="400" y="1140" text-anchor="middle">MARA QUELLTON</text>
  </g>
</svg>
</body>
</html>
```